Best Seller Book Cover ...

Book Title: Skip the Big Answer: Pick a Trail, Keep to That Trail, Mind the Geese

Edgy, Minimalist, Compelling, Attractive, Classy design.

Very clean. See examples.,

Target Market(s)

Mid Life People ages 38-55 Male and Female equally

• Nice to Have:

Minimalist and eye catching ( i have loaded a few examples of what this means)
Should not have
• Clip Art
Clutter

```html
<!DOCTYPE html>
<html lang="en">
<head>
<meta charset="utf-8">
<title>Skip the Big Answer — Book Cover</title>
<link rel="stylesheet" href="https://fonts.googleapis.com/css2?family=Oswald:wght@300;400;700&display=swap">
<style>
  :root {
    --backdrop: #e4e4e4;
    --paper: #ede2cb;
    --paper-light: #f4ecdb;
    --paper-stain: #e2cfae;
    --ink: #4a2320;
    --ink-soft: rgba(74, 35, 32, 0.55);
    --crease: rgba(120, 95, 70, 0.18);
  }
  * { margin: 0; padding: 0; box-sizing: border-box; }
  html, body {
    width: 921px;
    height: 1200px;
    overflow: hidden;
    background: var(--backdrop);
  }
  .canvas {
    position: relative;
    width: 921px;
    height: 1200px;
    display: flex;
    align-items: center;
    justify-content: center;
  }
  .cover {
    position: relative;
    width: 660px;
    height: 960px;
    background:
      radial-gradient(ellipse at 30% 40%, var(--paper-light) 0%, transparent 60%),
      radial-gradient(ellipse at 80% 85%, var(--paper-stain) 0%, transparent 55%),
      linear-gradient(160deg, var(--paper-light) 0%, var(--paper) 55%, var(--paper-stain) 100%);
    overflow: hidden;
  }
  .cover__creases {
    position: absolute;
    inset: 0;
    width: 100%;
    height: 100%;
    pointer-events: none;
  }
  .cover__title {
    position: absolute;
    top: 64px;
    left: 0;
    right: 0;
    text-align: center;
    color: var(--ink);
    font-family: 'Oswald', sans-serif;
    font-weight: 700;
    text-transform: uppercase;
    line-height: 1;
  }
  .cover__title-top {
    display: block;
    font-size: 66px;
    letter-spacing: 0.22em;
    margin-right: -0.22em;
  }
  .cover__title-main {
    display: block;
    font-size: 76px;
    letter-spacing: -0.01em;
    margin-top: 2px;
  }
  .cover__art {
    position: absolute;
    top: 380px;
    left: 50%;
    transform: translateX(-50%);
    width: 380px;
    height: 360px;
    border-radius: 45% 45% 40% 40%;
    background: radial-gradient(ellipse at center, rgba(92, 58, 45, 0.85) 0%, rgba(110, 75, 58, 0.55) 45%, rgba(150, 115, 90, 0) 72%);
  }
  .cover__subtitle {
    position: absolute;
    bottom: 70px;
    left: 50%;
    transform: translateX(-50%);
    color: var(--ink);
    font-family: 'Oswald', sans-serif;
    font-weight: 400;
    text-transform: uppercase;
    font-size: 32px;
    line-height: 1.02;
    text-align: center;
  }
  .cover__subtitle span { display: block; }
  .cover__subtitle .line-1 { letter-spacing: 0.42em; margin-right: -0.42em; }
  .cover__subtitle .line-2 { letter-spacing: 0.16em; margin-right: -0.16em; }
  .cover__subtitle .line-3 { letter-spacing: 0.2em; margin-right: -0.2em; }
</style>
</head>
<body>
  <main class="canvas">
    <article class="cover">
      <svg class="cover__creases" viewBox="0 0 660 960" preserveAspectRatio="none" aria-hidden="true">
        <line x1="330" y1="0" x2="330" y2="960" stroke="var(--crease)" stroke-width="2"/>
        <line x1="0" y1="470" x2="660" y2="500" stroke="var(--crease)" stroke-width="2"/>
        <line x1="0" y1="330" x2="660" y2="318" stroke="var(--crease)" stroke-width="1"/>
      </svg>

      <h1 class="cover__title">
        <span class="cover__title-top">Skip the Big</span>
        <span class="cover__title-main">Answer:</span>
      </h1>

      <div class="cover__art" role="img" aria-label="Symmetrical brown ink-blot illustration forming two mirrored animal silhouettes"></div>

      <p class="cover__subtitle">
        <span class="line-1">Pick a Trail</span>
        <span class="line-2">Keep to That Trail</span>
        <span class="line-3">Mind the Geese</span>
      </p>
    </article>
  </main>
</body>
</html>
```